Conference for Teenagers Needs Event Graphics

I am in need of event graphics for our upcoming event. This event, titled "Kestrel Youth Rally", is a weekend event for teenagers 11-19 years old. They hear from speakers, listen to a band, and do other fun activities. Our theme is "Together." Graphic design should have a young adult/older teen feel. Clean, not very bright colors.

Event Info:
November 6-8, 2020
Pellworth Exhibit Hall, Sioux Falls, SD
Speakers: TBD (will give name and picture before final approval)
Worship: (band name TBD before final approval)
KestrelYouthRally.com
#417KR
Our Organization Logo (attached): Lumen Forward

Once designed, I need the following graphics file sizes:
-11x17 Vertical Poster design: include all event info AND a "blank" spot/box for groups to add their own details/information. Also include the QRV logo and our organization logo Lumen Forward in someway.
-4x3 horizontal postcard: include all event info on 1 side including LumenForward logo and QRV; blank backside
-Main Graphic Slide: formatted to fit a widescreen 16x9 screen. Include event name, hashtag, QRV and Lumen Forward logo
-social media graphics for event: can incorporate some or all of the event details
-4.25x 2.75 vertical badge: include event title on front with Lumen Forward logo

Target Market(s)

Young adults or older teenagers

Requirements
Must have
• -event info
-Lumen Forward Logo & QRV logo

```html
<!DOCTYPE html>
<html lang="en">
<head>
<meta charset="utf-8">
<title>Kestrel Youth Rally Poster</title>
<link href="https://fonts.googleapis.com/css2?family=Krona+One&family=Lexend:wght@300;400;600&display=swap" rel="stylesheet">
<style>
  :root {
    --backdrop: #92c1ea;
    --poster-blue: #2b7bbb;
    --crowd-light: #5d9fd3;
    --crowd-dark: #2f6fa8;
    --white: #ffffff;
    --portrait: #d9e6f2;
  }
  * { margin: 0; padding: 0; box-sizing: border-box; }
  html, body {
    width: 1200px; height: 1200px; overflow: hidden;
    background: var(--backdrop);
    font-family: "Lexend", sans-serif;
    color: var(--white);
  }
  .poster {
    position: absolute; left: 175px; top: 50px;
    width: 850px; height: 1100px;
    background: var(--poster-blue);
    overflow: hidden;
  }
  .crowd-photo {
    position: absolute; left: 0; right: 0; top: 560px; bottom: 0;
    background:
      linear-gradient(180deg, var(--poster-blue) 0%, rgba(43,123,187,0.35) 25%, rgba(43,123,187,0.2) 100%),
      radial-gradient(ellipse at 30% 55%, var(--crowd-dark) 0%, transparent 45%),
      radial-gradient(ellipse at 75% 60%, var(--crowd-dark) 0%, transparent 40%),
      linear-gradient(180deg, var(--crowd-light), var(--crowd-light));
  }
  .content { position: relative; height: 100%; }
  .logos {
    position: absolute; left: 51px; top: 52px;
    display: flex; align-items: center; gap: 28px;
    font-family: "Lexend", sans-serif; font-weight: 600; font-size: 20px;
  }
  .logo { display: flex; align-items: center; gap: 8px; }
  .logo-dot { width: 14px; height: 14px; border-radius: 50%; background: var(--white); }
  .event-title {
    position: absolute; left: 51px; top: 150px;
    font-family: "Krona One", sans-serif; font-size: 62px; line-height: 80px;
    text-transform: lowercase;
    color: transparent; -webkit-text-stroke: 2.5px var(--white);
  }
  .event-details {
    position: absolute; left: 60px; top: 432px;
    font-size: 29px; font-weight: 300; line-height: 50px;
  }
  .section-divider {
    position: absolute; left: 51px; width: 748px;
    display: flex; align-items: center; gap: 18px;
    font-size: 29px; font-weight: 300;
  }
  .section-divider::before, .section-divider::after {
    content: ""; flex: 1; height: 3px; background: var(--white);
  }
  .speakers-divider { top: 566px; }
  .worship-divider { top: 851px; }
  .speakers {
    position: absolute; left: 0; top: 627px; width: 850px;
    display: flex; justify-content: center; gap: 58px;
  }
  .speaker { width: 130px; text-align: center; font-size: 22px; font-weight: 300; }
  .speaker-portrait {
    width: 130px; height: 130px; border-radius: 50%;
    background: var(--portrait); margin-bottom: 22px;
  }
  .band-name {
    position: absolute; left: 0; top: 912px; width: 850px; text-align: center;
    font-family: "Krona One", sans-serif; font-size: 30px; text-transform: lowercase;
  }
  .poster-footer {
    position: absolute; left: 51px; right: 51px; top: 1028px;
    display: flex; justify-content: space-between; font-size: 22px;
  }
  .website { font-style: italic; font-weight: 300; }
  .hashtag { font-weight: 600; font-style: italic; letter-spacing: 1px; }
</style>
</head>
<body>
  <main class="poster">
    <div class="crowd-photo" role="img" aria-label="Blurred photo of teenagers in a conference crowd, tinted blue"></div>
    <div class="content">
      <div class="logos">
        <div class="logo"><span class="logo-dot"></span>Lumen Forward</div>
        <div class="logo">QRV</div>
      </div>
      <h1 class="event-title">Kestrel<br>Youth<br>Rally</h1>
      <div class="event-details">
        <p>November 6-8, 2020</p>
        <p>Pellworth Exhibit Hall, Sioux Falls, SD</p>
      </div>
      <h2 class="section-divider speakers-divider">Speakers</h2>
      <div class="speakers">
        <div class="speaker"><div class="speaker-portrait" role="img" aria-label="Portrait of speaker John Doe"></div>John Doe</div>
        <div class="speaker"><div class="speaker-portrait" role="img" aria-label="Portrait of speaker Jane Roe"></div>Jane Roe</div>
        <div class="speaker"><div class="speaker-portrait" role="img" aria-label="Portrait of speaker Fred Nerks"></div>Fred Nerks</div>
        <div class="speaker"><div class="speaker-portrait" role="img" aria-label="Portrait of speaker Hilary Ouse"></div>Hilary Ouse</div>
      </div>
      <h2 class="section-divider worship-divider">Worship</h2>
      <p class="band-name">Band Name</p>
      <footer class="poster-footer">
        <span class="website">KestrelYouthRally.com</span>
        <span class="hashtag">#417KR</span>
      </footer>
    </div>
  </main>
</body>
</html>
```